Kid's Cancer Camp Business Card

Create a unique Two-Sided color business cards for Camp Willow Brook, a pediatric cancer camp.

The camp tag line is: Where every camper gets to just be a kid...

Dale Morrisey, Executive Director
Camp Willow Brook Charitable Foundation, Inc
PO Box 918
Kestrel Ridge, CT 06832

Phone - 203-555-0143
Fax - 203-555-0187
Email: dale@campwillowbrook.example
www.campwillowbrook.example

Target Market(s)

Potential Donors, Volunteers and Campers

Industry/Entity Type

Non-profit pediatric cancer camp

Contact Information for Business Card

All contact info that is included in the description

Font styles to use
Other font styles liked:
• Designer chooses font

Requirements
Must have
• Camp Willow Brook Logo and Tag Line
Nice to have
• should be eye catching
Should not have
• not cartoony

```html
<!DOCTYPE html>
<html lang="en">
<head>
<meta charset="utf-8">
<title>Camp Willow Brook – Business Card</title>
<link href="https://fonts.googleapis.com/css2?family=Montserrat:wght@400;500;700&display=swap" rel="stylesheet">
<style>
  :root {
    --canvas-bg: #d9d9d9;
    --card-white: #ffffff;
    --brand-blue: #1f6aa5;
    --deep-blue: #045c98;
    --light-blue: #4a8fba;
    --sun-yellow: #e9a81c;
    --sun-light: #fbbb33;
    --teal: #15a09a;
    --text-white: #ffffff;
  }
  * { box-sizing: border-box; margin: 0; padding: 0; }
  html, body {
    width: 1200px; height: 1200px; overflow: hidden;
    background: var(--canvas-bg);
    font-family: "Montserrat", Arial, sans-serif;
  }
  .sheet {
    width: 1200px; height: 1200px;
    display: flex; flex-direction: column; align-items: center; justify-content: center;
    gap: 60px;
  }
  .card {
    position: relative;
    width: 900px; height: 514px;
    border-radius: 28px;
    overflow: hidden;
    box-shadow: 0 8px 24px rgba(0,0,0,0.18);
  }
  /* Front */
  .card-front {
    background: var(--card-white);
    display: flex; flex-direction: column; align-items: center; justify-content: center;
    gap: 70px;
  }
  .wordmark { display: flex; align-items: center; gap: 18px; }
  .wordmark-dot {
    width: 40px; height: 40px; border-radius: 50%;
    background: var(--sun-light);
  }
  .wordmark-name {
    font-weight: 500; font-size: 52px; color: var(--brand-blue);
    letter-spacing: 0.5px; text-transform: lowercase;
  }
  .tagline {
    font-weight: 500; font-size: 26px; color: var(--teal); letter-spacing: 0.5px;
  }
  /* Back */
  .card-back {
    background: linear-gradient(90deg, var(--light-blue) 0%, var(--deep-blue) 55%, var(--deep-blue) 100%);
  }
  .contact-block {
    position: absolute; left: 70px; top: 90px;
    color: var(--text-white);
  }
  .person-name {
    font-weight: 700; font-size: 44px; color: var(--sun-yellow); line-height: 1.1;
  }
  .person-title { font-weight: 500; font-size: 24px; margin-top: 6px; }
  .address {
    font-weight: 500; font-size: 24px; line-height: 1.3; margin-top: 54px;
  }
  .contact-list { list-style: none; margin-top: 14px; }
  .contact-item {
    display: flex; align-items: center; gap: 14px;
    font-weight: 500; font-size: 23px; line-height: 1.5;
  }
  .contact-icon { width: 20px; height: 20px; fill: var(--sun-yellow); flex: none; }
  .sun-art {
    position: absolute; right: 0; top: 0;
    width: 300px; height: 514px;
    border-top-left-radius: 180px;
    background: linear-gradient(170deg, var(--sun-yellow) 0%, var(--sun-yellow) 60%, var(--teal) 82%, #eeeeee 100%);
  }
</style>
</head>
<body>
<main class="sheet">
  <section class="card card-front">
    <div class="wordmark">
      <span class="wordmark-dot"></span>
      <span class="wordmark-name">camp willow brook</span>
    </div>
    <p class="tagline">Where every camper gets to just be a kid...</p>
  </section>

  <section class="card card-back">
    <div class="sun-art" role="img" aria-label="Large decorative sun rising over teal waves"></div>
    <div class="contact-block">
      <h1 class="person-name">Dale Morrisey</h1>
      <p class="person-title">Executive Director</p>
      <p class="address">PO Box 918 Kestrel Ridge<br>CT 06832</p>
      <ul class="contact-list">
        <li class="contact-item">
          <svg class="contact-icon" viewBox="0 0 24 24"><path d="M6.6 10.8a15 15 0 0 0 6.6 6.6l2.2-2.2a1 1 0 0 1 1-.25 11.4 11.4 0 0 0 3.6.57 1 1 0 0 1 1 1V20a1 1 0 0 1-1 1A17 17 0 0 1 3 4a1 1 0 0 1 1-1h3.5a1 1 0 0 1 1 1c0 1.25.2 2.45.57 3.57a1 1 0 0 1-.25 1z"/></svg>
          203-555-0143
        </li>
        <li class="contact-item">
          <svg class="contact-icon" viewBox="0 0 24 24"><path d="M6 2h12v5H6zM3 8h18a2 2 0 0 1 2 2v7h-4v5H5v-5H1v-7a2 2 0 0 1 2-2zm4 8v4h10v-4z"/></svg>
          203-555-0187
        </li>
        <li class="contact-item">
          <svg class="contact-icon" viewBox="0 0 24 24"><path d="M2 5h20v14H2zm2 2v.5l8 5 8-5V7z"/></svg>
          dale@campwillowbrook.example
        </li>
        <li class="contact-item">
          <svg class="contact-icon" viewBox="0 0 24 24"><path d="M12 2a10 10 0 1 0 0 20 10 10 0 0 0 0-20zm6.9 9h-3a15 15 0 0 0-1.2-5.6A8 8 0 0 1 18.9 11zM12 4c1 1.3 1.8 3.8 1.9 7h-3.8C10.2 7.8 11 5.3 12 4zM9.3 5.4A15 15 0 0 0 8.1 11h-3a8 8 0 0 1 4.2-5.6zM5.1 13h3a15 15 0 0 0 1.2 5.6A8 8 0 0 1 5.1 13zM12 20c-1-1.3-1.8-3.8-1.9-7h3.8c-.1 3.2-.9 5.7-1.9 7zm2.7-1.4a15 15 0 0 0 1.2-5.6h3a8 8 0 0 1-4.2 5.6z"/></svg>
          www.campwillowbrook.example
        </li>
      </ul>
    </div>
  </section>
</main>
</body>
</html>
```